New Website Design & Build Project - Zestoria Meals

I am looking for a professional clean looking website design then build of a website for my meal delivery business Zestoria Meals. I already have the domain - www.zestoriameals.com.au and I will upload brief for the design and layout of the website.

I have a dropbox full of photos, designs, videos and existing graphic design work that I can share with the designers. This can be provided upon designer request.

I am looking to build this site in WORDPRESS and I would like to build the site using the Lumevo Page Composer - https://lumevothemes.com/

Target Market(s)

Kids from 2-16 , Teenagers - 16 - 19, Adults - 19 - 80 + - We Cater For Everyone

Industry/Entity Type

Health And Wellness

Coding

Coded - Design and coding required

Number of Pages Required

5+ page

Colors
33b8a4
abd037
ec1f27
fbee3f
3276b5

Requirements
Must have
• Must incorporate the included Zestoria Meals & ZM Logo
Must incorporate designs of packaging into website design.
Must keep text styles consistant throughout design
Must be mobile, tablet and desktop view responsive on all devices.
Must be built in Wordpress
The coder must have experience with lumevo themes, lumevo page composer, lumevo prospects and also be very experienced with setting up products using Cartavo Store plug in-
https://cartavostore.com/
I want to integrate Mailpiko - https://dealquarry.com/mailpiko/ into site as well
Nice to have
• All of the above
Should not have
• No dark colours

```html
<!DOCTYPE html>
<html lang="en">
<head>
<meta charset="utf-8">
<title>Zestoria Meals</title>
<link href="https://fonts.googleapis.com/css2?family=Montserrat:wght@400;500;600;700&display=swap" rel="stylesheet">
<style>
:root{
  --ink:#1b1b1b;
  --yellow:#fbee3f;
  --yellow-deep:#fad61e;
  --green:#abd037;
  --green-text:#8cc63f;
  --grey-band:#f4f4f4;
  --muted:#555;
  --white:#fff;
}
*{margin:0;padding:0;box-sizing:border-box}
html,body{width:1200px;height:2825px;overflow:hidden;background:var(--white)}
body{font-family:"Montserrat",sans-serif;color:var(--ink);position:relative}
.abs{position:absolute}
a{color:inherit}

/* header */
.site-header{position:absolute;left:0;top:0;width:1200px;height:60px;background:var(--white)}
.brand{position:absolute;left:89px;top:14px;display:flex;align-items:center;gap:8px;font-weight:700;font-size:24px;color:var(--ink);letter-spacing:.5px}
.brand-mark{width:14px;height:14px;background:var(--green)}
.nav-link{position:absolute;top:22px;font-size:15px;font-weight:500}
.nav-menu{left:409px;color:var(--green-text)}
.nav-contact{left:499px}
.nav-cart{left:636px;font-size:14.5px;display:flex;gap:6px;align-items:center}
.pill{position:absolute;border-radius:30px;display:flex;align-items:center;justify-content:center;font-weight:500}
.btn-login{left:840px;top:13px;width:130px;height:37px;background:var(--yellow);font-size:16px}
.btn-signup{left:979px;top:13px;width:130px;height:37px;background:var(--green);color:var(--white);font-size:16px}

/* hero (children positioned relative to hero, which starts at 60px) */
.hero{position:absolute;left:0;top:60px;width:1200px;height:580px}
.hero-brand{position:absolute;left:547px;top:138px;font-size:64px;line-height:1;font-weight:700;color:var(--ink);letter-spacing:-1px;white-space:nowrap}
.hero-tag{position:absolute;left:547px;top:232px;font-size:48px;line-height:1;font-weight:600;color:var(--green-text);white-space:nowrap;letter-spacing:-.3px}
.btn-order{left:547px;top:393px;width:183px;height:58px;background:var(--green);font-size:18px}

/* subscription */
.sub-title{position:absolute;left:0;width:1200px;top:716px;text-align:center;font-size:33px;font-weight:600}
.sub-text{position:absolute;left:0;width:1200px;top:768px;text-align:center;font-size:17px;font-weight:500}
.btn-join{left:530px;top:833px;width:139px;height:48px;background:var(--yellow);font-size:17px}

/* plans */
.plans{position:absolute;left:0;top:964px;width:1200px;height:574px;background:var(--grey-band)}
.plans-title{position:absolute;left:0;width:1200px;top:74px;text-align:center;font-size:34px;font-weight:600}
.plan{position:absolute;top:125px;width:217px}
.plan-photo{width:217px;height:260px;border-radius:3px}
.plan-name{margin-top:10px;font-size:19px;font-weight:500;line-height:22px}
.plan-price{margin-top:4px;padding-left:2px;font-size:18.5px;color:var(--green-text)}
.plan-join{display:block;margin-top:13px;padding-left:3px;font-size:13.5px;font-weight:500;text-decoration:underline}

/* smoothie band */
.smoothie{position:absolute;left:0;top:1538px;width:1200px;height:373px;background:linear-gradient(180deg,var(--green) 0%,#d8e23a 55%,var(--yellow) 100%)}
.smoothie-title{position:absolute;left:0;width:1200px;top:74px;text-align:center;font-size:34px;font-weight:700}
.smoothie-text{position:absolute;left:150px;width:900px;top:130px;text-align:center;font-size:16.5px;line-height:27px}
.btn-read{left:530px;top:241px;width:138px;height:49px;background:var(--green);font-size:16.5px}

/* blog */
.blog-title{position:absolute;left:0;width:1200px;top:1982px;text-align:center;font-size:49px;font-weight:600}
.post{position:absolute;top:2062px;width:331px}
.post-photo{width:331px;height:214px}
.post-card{position:absolute;left:14px;top:198px;width:304px;height:214px;background:var(--yellow);padding:24px 17px 0}
.post-card h3{font-size:18.5px;font-weight:500;line-height:25px}
.post-card p{margin-top:10px;font-size:12px;line-height:18px;color:#333}
.post-card a{display:block;margin-top:17px;font-size:15px;font-weight:600;text-decoration:none}

/* footer */
.foot-col{position:absolute;top:2556px;font-size:15px;line-height:24px;color:var(--muted)}
.foot-col h4{font-size:16px;font-weight:500;color:var(--ink);margin-bottom:10px}
.social{display:flex;align-items:center;gap:16px}
.social span.dot{width:10px;height:10px;border-radius:50%;background:#666}
.foot-rule{position:absolute;left:90px;top:2666px;width:1020px;height:1px;background:#e4e4e4}
.foot-brand{position:absolute;left:0;width:1200px;top:2712px;text-align:center;font-size:26px;font-weight:700}
.foot-small{position:absolute;left:0;width:1200px;text-align:center;font-size:12.5px;color:var(--muted)}
</style>
</head>
<body>

<header class="site-header">
  <div class="brand"><span class="brand-mark"></span>Zestoria Meals</div>
  <a class="nav-link nav-menu">MENU</a>
  <a class="nav-link nav-contact">CONTACT US</a>
  <a class="nav-link nav-cart">
    <svg width="15" height="13" viewBox="0 0 15 13"><path d="M0 1h3l2 7h8l2-6H4" fill="none" stroke="#1b1b1b" stroke-width="1.8"/><circle cx="6" cy="11" r="1.4" fill="#1b1b1b"/><circle cx="12" cy="11" r="1.4" fill="#1b1b1b"/></svg>
    Your Cart Has Empty</a>
  <a class="pill btn-login">LOGIN</a>
  <a class="pill btn-signup">SIGN UP</a>
</header>

<section class="hero">
  <svg class="abs" style="left:0;top:0" width="1200" height="580" viewBox="0 0 1200 580">
    <defs>
      <linearGradient id="heroYellow" x1="0" y1="0" x2="1" y2="0">
        <stop offset="0" stop-color="#fbee3f"/><stop offset="1" stop-color="#fad61e"/>
      </linearGradient>
      <linearGradient id="heroFood" x1="0" y1="0" x2="1" y2="1">
        <stop offset="0" stop-color="#e9c25a"/><stop offset=".45" stop-color="#8fbf4a"/><stop offset="1" stop-color="#d0553a"/>
      </linearGradient>
    </defs>
    <polygon points="0,0 1200,0 1200,532 949,580 592,508 252,580 0,541" fill="url(#heroYellow)"/>
    <polygon role="img" aria-label="Photo of prepared meals in trays: rice, salad and pasta with cutlery" points="0,0 500,0 260,580 0,541" fill="url(#heroFood)" opacity=".85"/>
    <circle cx="46" cy="291" r="23" fill="none" stroke="#1b1b1b" stroke-width="2.5" opacity=".5"/>
    <path d="M52 280 L38 291 L52 302 Z" fill="#1b1b1b" opacity=".5"/>
    <circle cx="1153" cy="291" r="23" fill="none" stroke="#1b1b1b" stroke-width="2.5"/>
    <path d="M1147 280 L1162 291 L1147 302 Z" fill="#1b1b1b"/>
  </svg>
  <div class="hero-brand">Zestoria Meals</div>
  <div class="hero-tag">VEGAN &amp; VEGETARIAN</div>
</section>
<a class="pill btn-order">ORDER NOW</a>

<h2 class="sub-title">Zestoria Meals Subscription Service</h2>
<p class="sub-text">Join the Zestoria Meals subscription service to get the lowest prices. Cancel anytime.</p>
<a class="pill btn-join">JOIN NOW</a>

<section class="plans">
  <h2 class="plans-title">Our Plan</h2>
  <div class="plan" style="left:136px">
    <div class="plan-photo" role="img" aria-label="Meal prep trays with chicken, sweet potato and broccoli" style="background:linear-gradient(135deg,#c9ccc8,#9fa39c 50%,#d1874a)"></div>
    <div class="plan-name">ZM Kids 7 Day<br>Meal Plan</div>
    <div class="plan-price">$35.00</div>
    <a class="plan-join">JOIN NOW</a>
  </div>
  <div class="plan" style="left:372px">
    <div class="plan-photo" role="img" aria-label="Child eating from a meal container at a table" style="background:linear-gradient(135deg,#d7d2cc,#a99f96 60%,#6f6660)"></div>
    <div class="plan-name">ZM Adult 7 Day Meal<br>Plan</div>
    <div class="plan-price">$54.00</div>
    <a class="plan-join">JOIN NOW</a>
  </div>
  <div class="plan" style="left:609px">
    <div class="plan-photo" role="img" aria-label="Spaghetti with tomato sauce and shaved cheese" style="background:linear-gradient(135deg,#c6562f,#e9c25a 50%,#f2dc78)"></div>
    <div class="plan-name">ZM Adult 7 Day<br>Couples Meal Plan</div>
    <div class="plan-price">$108.00</div>
    <a class="plan-join">JOIN NOW</a>
  </div>
  <div class="plan" style="left:846px">
    <div class="plan-photo" role="img" aria-label="Hands preparing fresh leafy salad" style="background:linear-gradient(160deg,#e8e3dd,#c9bfb2 50%,#5e8a3a)"></div>
    <div class="plan-name">ZM Adult 21 Meals Per<br>Week Plan</div>
    <div class="plan-price">$162.00</div>
    <a class="plan-join">JOIN NOW</a>
  </div>
</section>

<section class="smoothie">
  <h2 class="smoothie-title">The Best Green Smoothie To Start Your Day</h2>
  <p class="smoothie-text">The King of Green Smoothies would have to be my Superfood Green Smoothie which contains all the elements necessary for unbelievable muscle growth!!! In order to strip off the fat, add lean muscle mass &amp; to provide your body with all the best vitamins &amp; minerals try the following recipe.</p>
  <a class="pill btn-read">READ MORE</a>
</section>

<h2 class="blog-title">Latest Blog</h2>
<svg class="abs" style="left:30px;top:2229px" width="24" height="24" viewBox="0 0 24 24"><path d="M17 2 L7 12 L17 22" fill="none" stroke="#abd037" stroke-width="4"/></svg>
<svg class="abs" style="left:1146px;top:2229px" width="24" height="24" viewBox="0 0 24 24"><path d="M7 2 L17 12 L7 22" fill="none" stroke="#abd037" stroke-width="4"/></svg>

<article class="post" style="left:86px">
  <div class="post-photo" role="img" aria-label="Baguette sandwich with ham and tomato" style="background:linear-gradient(135deg,#5a4a3e,#d9a66b 50%,#b9473a)"></div>
  <div class="post-card">
    <h3>Fusce vitae lectus amet mi pulvinar maximus. Aenean placerat nibh accumsan</h3>
    <p>Nunc sit amet consequat risus. Curabitur ac elit leo. In eleifend dui tellus, in scelerisque elit porttitor et. Integer eu massa lacinia.</p>
    <a>READ MORE</a>
  </div>
</article>
<article class="post" style="left:431px">
  <div class="post-photo" role="img" aria-label="Raw dessert slices and coconut balls on a wooden board" style="background:linear-gradient(135deg,#d9b66a,#efe6d2 50%,#8a2a44)"></div>
  <div class="post-card">
    <h3>Sed libero felis, vestibulum et dolor eget, lacinia aliquet neque &nbsp;molestie.</h3>
    <p>Nunc sit amet consequat risus. Curabitur ac elit leo. In eleifend dui tellus, in scelerisque elit porttitor et. Integer eu massa lacinia.</p>
    <a>READ MORE</a>
  </div>
</article>
<article class="post" style="left:775px">
  <div class="post-photo" role="img" aria-label="Sliced chicken with broccoli and peppers" style="background:linear-gradient(135deg,#e9e4dc,#3f8a2e 50%,#d65a3c)"></div>
  <div class="post-card">
    <h3>Donec sit amet lectus nec mi tempor laoreet ac nec nunc auctor.</h3>
    <p>Nunc sit amet consequat risus. Curabitur ac elit leo. In eleifend dui tellus, in scelerisque elit porttitor et. Integer eu massa lacinia.</p>
    <a>READ MORE</a>
  </div>
</article>

<footer>
  <div class="foot-col" style="left:90px"><h4>Opening Hours</h4>Mon-Friday : 9 am to 5 pm<br>Sat : 8 am to 12 pm</div>
  <div class="foot-col" style="left:391px"><h4>Contact Us</h4>0400 118 552<br>hello@zestoriameals.com.au</div>
  <div class="foot-col" style="left:745px"><h4>Follow Us</h4>
    <div class="social"><span class="dot"></span>Friendloop</div>
    <div class="social"><span class="dot"></span>Snapgrid</div>
  </div>
  <div class="foot-col" style="left:974px;top:2566px">Disclaimer<br>Terms &amp; Conditions<br>Privacy Policy</div>
  <div class="foot-rule"></div>
  <div class="foot-brand">ZM</div>
  <div class="foot-small" style="top:2764px">27 Orchard Lane,Greenvale,QLD,4100</div>
  <div class="foot-small" style="top:2791px">Copyright2020 Zestoria Meals Pty Ltd.ABN - 12345678901</div>
</footer>

</body>
</html>
```